依頼詳細
[ 歯科医院の特徴 ]
◆ ターゲット層
30代〜40代の女性がメインターゲット

派生してお子さんや年配の方までが通いやすい、
『家族で通えるような歯科医院』

◆ 推していく診療
オールマイティな診療(総合歯科診療)を行いつつ、
予防歯科・矯正歯科(Vuxa有り)・CAD/CAM(ミロナ)の患者を獲得。

◆ サイトで伝えていきたいこと
予防歯科の重要性
感染予防対策が行われている医院
早く、精密に行えるデジタルな診療

◆ 好きなサイトテイスト
https://www.wavelid-dentaloffice.example/

現代のサイトデザインの流行を取り入れ、
おしゃれではあるもののユーザーファーストなデザインを希望いたします。

また、Javascriptで多少のフェードインを想定しておりますので、
それに伴ったデザインを構成していただけますと幸いです。

内装パースデザイン, ロゴデザインを添付しております。
ご覧いただき、一貫性のあるサイトデザインをご提案いただけますと幸いです。

◆ 診療理念
患者様の笑顔と健康をサポートする
◇ 患者様によく説明し、納得、理解していただき歯科治療を行う
◇ 最新歯科治療、技術、サービスの日々研鑚取得
◇ 痛みの少ない治療の実施、低侵襲治療
◇ 行き届いた滅菌、衛生管理
◇ 自らの家族を呼べるような場所

◆ 医院の特徴
・可能な限り抜かない、削らない低侵襲治療(予防歯科の推奨)
・先進医療機器で治療の可能性を最大限に。
・安心して治療が受けられる衛生管理徹底
・矯正担当医によるソルテミーナ矯正・小児矯正
・患者様が通いやすい土日診療

◆ 診療時間
診療時間   月 火 水 木 金 土 日
09:30-13:00 ○ - ○ ○ ○ ○ ○
14:30-18:30 ○ - ○ ○ ○ ▲ ▲
▲:土日 (14:30-17:00)
休診日:火曜・祝日

◆ 院内紹介
①待合室
患者様に明るく広いリラックスできる空間を心がけています。

②キッズルーム
キッズルームやおむつ交換台もあるのでお子様連れのお母さんも安心です。

③完全バリアフリー設計
駐車場から治療室までバリアフリー設計になっています。ベビーカーでそのまま入れます。

④カウセリングルーム
お悩み事や診療への不安など気軽に相談ください。現在のお口の状態、治療計画、診療費用などをモニターを用いてご説明します。

⑤個室診療室
配慮したい時や、精密な治療などを行うときのために、個室診療室をご用意いたしました。静かな環境で、治療をお受けください。

⑥口腔外バキューム
歯の削りかすや血液などが空気中に飛び散るのを防ぐために口腔外バキュームを採用しております。口腔外バキュームは、口腔内バキュームの約2倍の吸収率で、粉塵を確実に吸い取ります。院内の衛生管理に、欠かせないアイテムです。
サイトURL
ページ数
1ページ
希望イメージ
シンプル 複雑
単色 カラフル
暗い 明るい
日常 高級
遊び心 厳粛
未来的 伝統的
女性的 男性的
希望する色
青系、水色系、茶系
納品ファイル
• 高解像度JPG (.jpg)
• イラストレーター形式 (.ai)
• PNG形式 (.png)
補足説明
TOPページだけでなく、SUBページもお願いできればと思い、
この度延長をいたしました。

◇ TOPページのデザイン(レスポンシブ)

◇ SUBページのテンプレートデザイン(レスポンシブ)
テンプレート化してそれを元に他ページを作成できるよう、
見出しタグや画像を使用した際のレイアウト例をお願いいたします。
[ 参考:https://www.tomorane-shika.example/sub.html ]

```html
<!DOCTYPE html>
<html lang="ja">
<head>
<meta charset="utf-8">
<title>HARU DENTAL CLINIC</title>
<link rel="stylesheet" href="https://fonts.googleapis.com/css2?family=Noto+Sans+JP:wght@400;500;700&family=Noto+Serif+JP:wght@400;500;600&family=Cormorant+Garamond:wght@500;600&display=swap">
<style>
:root{
  --ink:#3d4b5a;
  --ink-soft:#6b7886;
  --accent:#8cc3ec;
  --accent-deep:#5c9fd6;
  --pale:#eaf3fb;
  --footer:#72acde;
  --line:#c9d9e8;
  --white:#ffffff;
}
*{margin:0;padding:0;box-sizing:border-box}
html,body{width:1200px;height:4920px;overflow:hidden}
body{position:relative;background:var(--white);color:var(--ink);font-family:"Noto Sans JP",sans-serif}
.abs{position:absolute}
.fill{position:absolute;display:block}
.serif{font-family:"Noto Serif JP",serif}

/* header / hero */
.hero{left:0;top:0;width:1200px;height:740px;background:linear-gradient(135deg,#cfe0ee 0%,#eef3f7 45%,#a9c6de 100%)}
.logo{left:40px;top:26px;display:flex;align-items:center;gap:12px;color:var(--white);font-weight:700;font-size:26px;letter-spacing:1px}
.logo .dot{width:30px;height:30px;border-radius:50%;background:var(--white)}
.nav{right:60px;top:36px;display:flex;gap:120px;font-size:15px;color:var(--ink)}
.hero-copy{left:560px;top:560px;width:620px;padding:26px 40px;background:rgba(255,255,255,.82);font-family:"Noto Serif JP",serif;color:var(--ink)}
.hero-copy p{font-size:34px;line-height:1.55;letter-spacing:2px;font-weight:500}
.pager{left:0;top:770px;width:1200px;display:flex;justify-content:center;gap:10px}
.pager i{width:8px;height:8px;border-radius:50%;background:var(--ink)}
.pager i:first-child{background:var(--accent)}

/* notice */
.notice{left:240px;top:835px;width:520px;height:120px;background:linear-gradient(90deg,#9cc9ea,#cfe6f6);border:4px solid var(--white);outline:2px solid var(--line);text-align:center;color:var(--white);font-family:"Noto Serif JP",serif;padding-top:20px}
.notice h3{font-size:28px;font-weight:500;letter-spacing:2px}
.notice p{font-size:17px;margin-top:8px}

/* section headings */
.heading{left:0;width:1200px;text-align:center;font-family:"Noto Serif JP",serif}
.heading h2{font-size:26px;font-weight:500;letter-spacing:3px}
.heading span{display:block;font-family:"Cormorant Garamond",serif;font-size:17px;letter-spacing:2px;color:var(--ink-soft);margin-top:2px}
.lead{left:0;width:1200px;text-align:center;font-size:16px;line-height:1.9;color:var(--ink-soft)}

/* policy */
.policy-lead{left:130px;top:1510px;width:420px;font-family:"Noto Serif JP",serif;font-size:26px;line-height:1.75;letter-spacing:1px}
.policy-points{left:630px;top:1510px;width:440px}
.point{margin-bottom:44px}
.point h3{font-family:"Noto Serif JP",serif;font-size:20px;font-weight:500;padding-bottom:8px;border-bottom:1px solid var(--line)}
.point h3 b{font-weight:500;margin-right:28px}
.point p{font-size:13px;line-height:1.9;color:var(--ink-soft);margin-top:12px}

/* buttons */
.btn{width:280px;height:66px;border-radius:33px;background:var(--accent);color:var(--white);text-align:center;padding-top:12px;box-shadow:0 3px 8px rgba(92,159,214,.25)}
.btn strong{display:block;font-size:17px;font-weight:500;letter-spacing:1px}
.btn small{display:block;font-family:"Cormorant Garamond",serif;font-size:12px;letter-spacing:1px}

/* features */
.card{width:240px;height:400px;background:var(--pale);box-shadow:0 2px 6px rgba(60,90,120,.08)}
.card .photo{width:240px;height:170px}
.card h3{font-family:"Noto Serif JP",serif;font-size:21px;font-weight:500;text-align:center;line-height:1.5;padding:0 10px;margin-top:54px;min-height:64px}
.card p{font-size:12px;line-height:1.9;text-align:center;color:var(--ink-soft);margin-top:16px;padding:0 16px}

/* treatments */
.treat{width:200px;text-align:center}
.treat .icon{width:90px;height:90px;margin:0 auto;border-radius:50%;background:var(--pale)}
.treat small{display:block;font-family:"Cormorant Garamond",serif;font-size:14px;color:var(--ink-soft);margin-top:10px}
.treat strong{display:block;font-size:20px;font-weight:500;color:var(--accent-deep);padding-bottom:6px;border-bottom:1px solid var(--accent);width:130px;margin:2px auto 0}

/* introduction */
.fac{width:180px;text-align:center;font-size:15px}
.fac .icon{width:90px;height:90px;margin:0 auto 14px;border-radius:16px;background:var(--pale)}
.room-text{left:680px;top:4030px;width:400px}
.room-text h3{font-family:"Noto Serif JP",serif;font-size:24px;font-weight:500}
.room-text p{font-size:14px;line-height:1.9;color:var(--ink-soft);margin-top:14px}

/* footer */
.footer{left:0;top:4380px;width:580px;height:540px;background:var(--footer);color:var(--white);padding:44px 0 0 60px}
.footer .logo{position:static;font-size:34px}
.footer .logo .dot{width:40px;height:40px}
.footer .tel{font-size:24px;margin-top:22px;letter-spacing:1px}
.hours{margin-top:14px;border-collapse:collapse;font-size:22px}
.hours td{padding:2px 0;letter-spacing:4px}
.hours td:first-child{width:190px;letter-spacing:1px}
.footer .note{font-size:22px;margin-top:4px}
.map{left:580px;top:4380px;width:620px;height:540px;background:linear-gradient(135deg,#e3ecdf,#f2f2ee 50%,#dfe8ee)}
</style>
</head>
<body>

<header>
  <div class="fill hero" role="img" aria-label="患者の口元を診察するマスク姿の歯科医師の写真"></div>
  <div class="abs logo"><span class="dot"></span>HARU DENTAL CLINIC</div>
  <nav class="abs nav"><span>当院について</span><span>アクセス</span></nav>
  <div class="abs hero-copy"><p>治療から予防へ<br>あなたの大切な歯を守ります。</p></div>
  <div class="abs pager"><i></i><i></i><i></i></div>
</header>

<a class="abs notice">
  <h3>院内感染予防に力をいれています</h3>
  <p>当院の感染対策について &gt;</p>
</a>

<section>
  <div class="abs heading" style="top:1000px"><h2>診療理念</h2><span>Policy</span></div>
  <div class="fill" style="left:0;top:1070px;width:1200px;height:400px;background:linear-gradient(180deg,#f4f6f8,#e4ebf1)" role="img" aria-label="白衣の歯科スタッフ三名の写真"></div>
  <p class="abs policy-lead">当院は、小さなお子さんから<br>お年寄りの方まで、<br>ご家族で歯科治療を<br>受けていただける<br>デンタルクリニックです。</p>
  <div class="abs policy-points">
    <div class="point"><h3><b>1</b>先進的医療の提供</h3><p>当院では、患者様によく説明し、納得と理解をいただいた上で、最新のデジタル歯科機器を活用し、痛みの少ない治療を行います。</p></div>
    <div class="point"><h3><b>2</b>予防歯科の推奨</h3><p>歯科衛生士による定期検診とクリーニングで、可能な限り抜かない、削らない治療を目指し、ご家族の歯の健康を長く守ります。</p></div>
  </div>
  <a class="abs btn" style="left:460px;top:1860px"><strong>詳細はこちら</strong><small>Reasons</small></a>
</section>

<section>
  <div class="abs heading" style="top:1960px"><h2>当院の特徴</h2><span>FEATURES</span></div>
  <p class="abs lead" style="top:2040px">患者様にご納得・ご理解いただける歯科治療をおこないます。<br>最新歯科治療を取り入れながら診療いたします。</p>

  <div class="abs card" style="left:208px;top:2160px"><div class="photo" style="background:linear-gradient(135deg,#f1e6df,#d8e6f0)" role="img" aria-label="歯のクリーニングを受ける女性の写真"></div><h3>予防歯科の推奨</h3><p>定期検診で虫歯や歯周病を早期に発見し、歯を守ります。</p></div>
  <div class="abs card" style="left:480px;top:2160px"><div class="photo" style="background:linear-gradient(135deg,#e6edf2,#c9d9e6)" role="img" aria-label="治療器具の写真"></div><h3>痛みの少ない<br>治療の実施</h3><p>可能な限り抜かない、削らない低侵襲治療です。</p></div>
  <div class="abs card" style="left:760px;top:2160px"><div class="photo" style="background:linear-gradient(135deg,#e9ecef,#c7d3dd)" role="img" aria-label="診療チェアと先進医療機器の写真"></div><h3>先進医療機器</h3><p>精密で早いデジタル診療で治療の可能性を最大限に。</p></div>

  <div class="abs card" style="left:208px;top:2590px"><div class="photo" style="background:linear-gradient(135deg,#efe2d8,#d9c8bb)" role="img" aria-label="歯を見せて笑う子どもの写真"></div><h3>ソルテミーナ矯正<br>小児矯正</h3><p>矯正担当医による目立ちにくい矯正と小児矯正です。</p></div>
  <div class="abs card" style="left:480px;top:2590px"><div class="photo" style="background:linear-gradient(135deg,#e2eef0,#c5dde2)" role="img" aria-label="滅菌器の写真"></div><h3>衛生管理の徹底</h3><p>行き届いた滅菌で安心して治療を受けられます。</p></div>
  <div class="abs card" style="left:760px;top:2590px"><div class="photo" style="background:linear-gradient(135deg,#f3ebe4,#e0d2c6)" role="img" aria-label="子どもを抱く母親の写真"></div><h3>土日診療</h3><p>平日忙しい方も土日に通院できます。</p></div>

  <a class="abs btn" style="left:460px;top:3010px"><strong>詳細はこちら</strong><small>Features</small></a>
</section>

<section>
  <div class="abs heading" style="top:3160px"><h2>診療案内</h2><span>TREATMENTS</span></div>
  <div class="abs treat" style="left:270px;top:3240px"><div class="icon" role="img" aria-label="歯のアイコン"></div><small>Prevention</small><strong>予防歯科</strong></div>
  <div class="abs treat" style="left:500px;top:3240px"><div class="icon" role="img" aria-label="矯正装置のアイコン"></div><small>Orthodontics</small><strong>矯正歯科</strong></div>
  <div class="abs treat" style="left:730px;top:3240px"><div class="icon" role="img" aria-label="被せ物の歯のアイコン"></div><small>promotion</small><strong>CAD/CAM</strong></div>
  <p class="abs lead" style="top:3420px">総合歯科診療をはじめ、様々なアプローチで患者様の笑顔と健康をサポートします。</p>
  <a class="abs btn" style="left:460px;top:3490px"><strong>詳細はこちら</strong><small>Treatments</small></a>
</section>

<section>
  <div class="abs heading" style="top:3630px"><h2>院内紹介</h2><span>Introduction</span></div>
  <p class="abs lead" style="top:3710px">バリアフリー・キッズスペースを準備しておりますので<br>患者様・ご家族もご一緒にお越しいただけます。</p>
  <div class="abs fac" style="left:290px;top:3810px"><div class="icon" role="img" aria-label="車椅子のアイコン"></div>バリアフリー</div>
  <div class="abs fac" style="left:510px;top:3810px"><div class="icon" role="img" aria-label="親子のアイコン"></div>キッズスペース</div>
  <div class="abs fac" style="left:730px;top:3810px"><div class="icon" role="img" aria-label="カルテのアイコン"></div>カウセリング個室</div>
  <div class="fill" style="left:150px;top:3980px;width:400px;height:330px;background:linear-gradient(135deg,#f4efe8,#dcc9b4)" role="img" aria-label="木目の受付カウンターがある明るい待合室の写真"></div>
  <div class="abs room-text"><h3>リラックス出来る空間</h3><p>キッズルーム・バリアフリー、<br>カウセリング個室完備。<br>リラックスしてお待ちいただけます。</p></div>
  <a class="abs btn" style="left:700px;top:4220px"><strong>院内紹介はこちら</strong><small>Introduction</small></a>
</section>

<footer>
  <div class="abs footer">
    <div class="logo"><span class="dot"></span>HARU DENTAL CLINIC</div>
    <p class="tel">TEL:000-000-0000</p>
    <table class="hours">
      <tr><td>診療時間</td><td>月火水木金土日</td></tr>
      <tr><td>09:30-13:00</td><td>○-○○○○○</td></tr>
      <tr><td>14:30-18:30</td><td>○-○○○▲▲</td></tr>
    </table>
    <p class="note">▲：土日（14:30-17:00）</p>
    <p class="note">休診日：火曜・祝日</p>
  </div>
  <div class="fill map" role="img" aria-label="医院周辺の地図"></div>
</footer>

</body>
</html>
```